Creative design for PLW Businesscard!

We would like a creative business card for our company The Maple Workshop. We situated in Barcelona and setup software development teams for companies in Belgium, Holland.

Orange is related to Holland.
PLW means cool in Dutch

* An Overview / Background of the Business & Services
o Setup and manage developer teams in Barcelona for for companies
in Holland, Belgium.
* The Target Market / Audience you are trying to reach
o Companies in Holland searching for developers
* Design Specifics; any preferences or ideas for Style, Colour,
Imagery, etc
o Orange, professional, fancy
o The Maple Workshop (PLW) means cool , good, nice

Target Market(s)

Companies in Holland searching for developers

Industry/Entity Type

Business

Contact Information for Business Card

Company name: The Maple Workshop

Name: Joost ter Haarveld

Title: Managing director (not necessary)

Email: joost@themapleworkshop.es

web: www.themapleworkshop.es

Phone: (+34) 932 487 113

Mobile: (+34) 668 302 947

Font styles to use
Other font styles liked:
• Bookman Old Style or Rockwell

Requirements
Must have
• Setup and manage developer teams in Barcelona for for companies
• in Holland, Belgium.

```html
<!DOCTYPE html>
<html lang="en">
<head>
<meta charset="utf-8">
<title>The Maple Workshop – Business Card</title>
<link rel="stylesheet" href="https://fonts.googleapis.com/css2?family=Montserrat:wght@500;600;700&display=swap">
<style>
  :root {
    --backdrop: #e4e4e4;
    --paper: #ffffff;
    --charcoal: #3c3c3b;
    --charcoal-deep: #2e2e2d;
    --ink: #2b2b2b;
    --orange: #e8743b;
  }
  * { box-sizing: border-box; margin: 0; padding: 0; }
  html, body { width: 1200px; height: 800px; overflow: hidden; }
  body {
    background: var(--backdrop);
    font-family: "Montserrat", sans-serif;
    display: flex;
    align-items: center;
    justify-content: center;
    gap: 40px;
  }
  .card {
    position: relative;
    width: 550px;
    height: 314px;
    overflow: hidden;
    box-shadow: 0 2px 6px rgba(0,0,0,0.18);
  }
  /* Front side */
  .card--front { background: var(--paper); color: var(--ink); }
  .brand {
    position: absolute;
    top: 38px;
    right: 60px;
    width: 200px;
    text-align: center;
  }
  .brand__name {
    font-weight: 700;
    font-size: 50px;
    line-height: 1;
    color: var(--ink);
    letter-spacing: 2px;
  }
  .brand__tagline {
    margin-top: 8px;
    font-weight: 500;
    font-size: 15px;
    color: var(--orange);
    letter-spacing: 0.3px;
  }
  .person {
    position: absolute;
    left: 40px;
    top: 122px;
  }
  .person__name {
    font-weight: 600;
    font-size: 27px;
    letter-spacing: 0.4px;
    color: var(--ink);
  }
  .person__role {
    font-weight: 500;
    font-size: 18px;
    color: var(--orange);
    margin-top: -2px;
  }
  .contact {
    position: absolute;
    left: 34px;
    top: 200px;
    list-style: none;
    font-size: 15px;
    line-height: 23px;
    font-weight: 500;
  }
  .contact__label { color: var(--orange); }
  .contact__value { color: var(--ink); }
  .swoosh {
    position: absolute;
    right: 0; bottom: 0;
    width: 550px; height: 314px;
  }
  /* Back side */
  .card--back {
    background: var(--charcoal);
    display: flex;
    align-items: center;
    justify-content: center;
  }
  .back__name {
    font-weight: 700;
    font-size: 120px;
    line-height: 1;
    color: var(--charcoal-deep);
    letter-spacing: 6px;
  }
</style>
</head>
<body>
  <section class="card card--front" aria-label="Business card front">
    <svg class="swoosh" viewBox="0 0 550 314" aria-hidden="true">
      <path d="M550 190 C 470 250 400 290 330 314 L550 314 Z" fill="var(--charcoal)"/>
      <path d="M505 218 C 440 260 380 290 310 306 L300 314 C 380 300 450 262 505 218 Z" fill="var(--orange)"/>
    </svg>

    <div class="brand">
      <p class="brand__name">PLW</p>
      <p class="brand__tagline">The Maple Workshop</p>
    </div>

    <div class="person">
      <h1 class="person__name">Joost ter Haarveld</h1>
      <p class="person__role">Managing director</p>
    </div>

    <ul class="contact">
      <li><span class="contact__label">Mobile : </span><span class="contact__value">(+34) 668 302 947</span></li>
      <li><span class="contact__label">Phone : </span><span class="contact__value">(+34) 932 487 113</span></li>
      <li><span class="contact__label">Email : </span><span class="contact__value">joost@themapleworkshop.es</span></li>
      <li><span class="contact__label">Website : </span><span class="contact__value">www.themapleworkshop.es</span></li>
    </ul>
  </section>

  <section class="card card--back" aria-label="Business card back">
    <span class="back__name">PLW</span>
  </section>
</body>
</html>
```